Website Re-design

Hi, I'm looking for help in redesigning my web site. I currently have a site www.brightnookwares.example where I sell lamps, and while I like some aspects of the design, you can tell that I have done the graphics myself and am not a pro at it. I'd like help in redesigning it, and am open to completely new design graphics. I have made the 3 slider images myself, and I feel they could be a bit better, but I am not sure how to do it. For example, on the homepage, the 'About Us', 'Secured Shopping', and '$10 Off' graphics don't go well with the rest of the page. I would like more cohesion in the design and more visual interest in the header, which is pretty basic right now. Also, that the bottom footer is black, I would like instead something else. I am looking for just the layout of the homepage, and possibly once that is done to work on more visual interest in some of the informational pages and product pages. I am looking for just the design in the form of a photoshop file or files that I can incorporate into my site. Thank you!

Reason: I just made this project payment committed, so I'd like a chance for designers who only choose payment committed projects to submit artwork. Thank you.

This project is now payment guaranteed/ committed.  Thanks.

```html
<!DOCTYPE html>
<html lang="en">
<head>
<meta charset="utf-8">
<title>Bright Nook Wares — Home</title>
<link href="https://fonts.googleapis.com/css2?family=Questrial&family=Source+Sans+3:wght@400;600&display=swap" rel="stylesheet">
<style>
:root{
  --teal:#5bb9bd;
  --teal-dark:#2f8f96;
  --nav-active:#1f6f9e;
  --text:#4a4a4a;
  --muted:#666;
  --rule:#cfcfcf;
  --bar:#f0f0f0;
  --white:#fff;
}
*{box-sizing:border-box;margin:0;padding:0}
html,body{width:1184px;height:1200px;overflow:hidden;background:var(--white)}
body{font-family:"Source Sans 3",Arial,sans-serif;color:var(--text)}
.page{position:relative;width:1400px;height:1419px;transform:scale(0.845714);transform-origin:0 0}
.abs{position:absolute}

.topbar{left:0;top:0;width:1400px;height:54px;background:var(--bar)}
.topbar .link{top:19px;font-size:13px;color:#555}
.topbar .sep{left:810px;top:18px;font-size:14px;color:#555}
.btn-outline{top:11px;height:32px;border:1px solid #777;font-size:13px;color:#555;display:flex;align-items:center;justify-content:center;gap:6px}

.brand{left:210px;top:70px;display:flex;align-items:center;gap:12px}
.brand .mark{width:62px;height:62px;border:3px solid #444;border-radius:50%}
.brand .name{font-size:30px;line-height:32px;color:#444;font-weight:600;width:170px}
.nav{top:100px;font-size:14px;color:#666}
.nav.active{color:var(--nav-active)}
.header-rule{left:210px;top:160px;width:980px;height:1px;background:var(--rule)}

.hero{left:210px;top:183px;width:980px;height:576px;overflow:hidden}
.hero-photo{position:absolute;inset:0;background:
  linear-gradient(180deg,rgba(0,0,0,0) 79%,#d9dfe0 80%,#f3f5f5 100%),
  radial-gradient(ellipse at 80% 40%,#a5e6e6 0%,#6ec4c4 45%,#3d9a9c 100%)}
.hero-lamp{position:absolute;left:665px;top:97px;width:260px;height:440px;background:linear-gradient(180deg,#f2f2f2 0 40%,#3aa3c4 55%,#6fb65a 100%);border-radius:8px 8px 60px 60px;opacity:.85}
.hero-title{position:absolute;left:0;width:690px;text-align:center;top:160px;font-family:"Questrial",sans-serif;font-size:60px;color:var(--white)}
.hero-sub{position:absolute;left:0;width:690px;text-align:center;top:252px;font-family:"Questrial",sans-serif;font-size:30px;color:var(--white)}
.hero-btn{position:absolute;left:169px;top:321px;width:321px;height:67px;border:1px solid var(--white);padding:2px}
.hero-btn span{display:flex;align-items:center;justify-content:center;gap:14px;width:100%;height:100%;border:2px solid var(--white);font-family:"Questrial",sans-serif;font-size:28px;color:var(--white)}
.dots{position:absolute;right:15px;top:549px;display:flex;gap:6px}
.dots i{width:15px;height:15px;border:1px solid var(--white)}
.dots i.on{background:var(--white)}

.welcome{left:210px;top:788px;width:980px;text-align:center;font-size:26px;color:var(--teal)}
.intro{left:210px;top:832px;width:980px;text-align:center;font-size:16px;line-height:25px;color:#555}

.card{top:912px;width:319px;height:183px;overflow:hidden}
.card .photo{position:absolute;inset:0}
.card .caption{position:absolute;left:0;bottom:0;width:100%;height:36px;background:rgba(30,30,30,.72);display:flex;align-items:center;justify-content:space-between;padding:0 10px 0 18px}
.card .caption b{font-weight:400;font-size:18px;color:var(--white)}
.card .caption small{font-size:10px;color:var(--white);display:flex;gap:4px;align-items:center}
.card-text{top:1110px;width:300px;font-size:13px;line-height:21px;color:#555}

.footer-rule{left:210px;top:1189px;width:980px;height:1px;background:var(--rule)}
.fcol{top:1210px}
.fcol h3{font-weight:400;font-size:15px;color:var(--teal);margin-bottom:8px}
.fcol li{list-style:none;font-size:9.5px;line-height:18px;color:#555;text-transform:uppercase}
.fcol li::before{content:"›";color:#999;margin-right:6px}
.fdiv{top:1217px;width:1px;height:113px;background:var(--rule)}
.newsletter p{font-size:11px;margin:4px 0 8px 2px;color:#444}
.email{width:246px;height:24px;border:1px solid #ccc;font-size:9px;color:#666;padding:6px 10px}
.submit{position:absolute;right:0;top:88px;width:67px;height:21px;background:#3e4146;color:var(--white);font-size:11px;display:flex;align-items:center;justify-content:center}

.bottombar{left:210px;top:1375px;width:980px;height:44px;background:var(--bar)}
.bottombar .copy{position:absolute;left:23px;top:15px;font-size:11px;color:#444}
.bottombar .follow{position:absolute;right:122px;top:15px;font-size:11px;color:#444}
.social{position:absolute;top:7px;width:29px;height:29px;border-radius:50%}
</style>
</head>
<body>
<div class="page">

  <div class="abs topbar">
    <span class="abs link" style="left:624px">Sign in or Create an account</span>
    <span class="abs sep">|</span>
    <span class="abs link" style="left:848px">My Account</span>
    <div class="abs btn-outline" style="left:941px;width:118px">View Cart
      <svg width="11" height="9" viewBox="0 0 11 9"><path d="M1 1l3.5 3.5L1 8M6 1l3.5 3.5L6 8" fill="none" stroke="#666" stroke-width="1.4"/></svg></div>
    <div class="abs btn-outline" style="left:1071px;width:118px">Checkout
      <svg width="11" height="9" viewBox="0 0 11 9"><path d="M1 1l3.5 3.5L1 8M6 1l3.5 3.5L6 8" fill="none" stroke="#666" stroke-width="1.4"/></svg></div>
  </div>

  <div class="abs brand">
    <div class="mark"></div>
    <div class="name">bright nook wares</div>
  </div>
  <span class="abs nav active" style="left:742px">HOME</span>
  <span class="abs nav" style="left:856px">SHOP</span>
  <span class="abs nav" style="left:967px">ABOUT US</span>
  <span class="abs nav" style="left:1104px">CONTACT US</span>
  <div class="abs header-rule"></div>

  <section class="abs hero">
    <div class="hero-photo" role="img" aria-label="Teal wall and pale wooden floor with a blue glass table lamp and white shade"></div>
    <div class="hero-lamp" role="img" aria-label="Blue glass table lamp with white shade"></div>
    <h1 class="hero-title" style="font-weight:400">Light up the Room</h1>
    <p class="hero-sub">" The Lagoon" Medium table Lamp</p>
    <div class="hero-btn"><span>Show all lamps
      <svg width="24" height="20" viewBox="0 0 24 20"><path d="M2 2l8 8-8 8M12 2l8 8-8 8" fill="none" stroke="#fff" stroke-width="3"/></svg></span></div>
    <div class="dots"><i class="on"></i><i></i><i></i><i></i></div>
  </section>

  <h2 class="abs welcome" style="font-weight:400">WELCOME TO BRIGHT NOOK WARES</h2>
  <p class="abs intro">Bright Nook Wares was born out of an enthusiasm for creating visually enticing forms combined with a strong sense of the way that lighting sets the mood and frames a space.</p>

  <article class="abs card" style="left:210px">
    <div class="photo" role="img" aria-label="Warm lit table lamp with dark shade on a wooden side table" style="background:radial-gradient(circle at 40% 35%,#f0a040 0%,#a0501a 45%,#3a1a0a 100%)"></div>
    <div class="caption"><b>ABOUT US</b><small>READMORE <svg width="9" height="8" viewBox="0 0 9 8"><path d="M1 1l3 3-3 3M5 1l3 3-3 3" fill="none" stroke="#fff" stroke-width="1.4"/></svg></small></div>
  </article>
  <article class="abs card" style="left:540px">
    <div class="photo" role="img" aria-label="Shopping cart icon on a computer key" style="background:radial-gradient(circle at 55% 40%,#f2f5f7 0%,#b9d0dc 45%,#4f7f95 100%)"></div>
    <div class="caption"><b>SECURED SHOPPING</b><small>READMORE <svg width="9" height="8" viewBox="0 0 9 8"><path d="M1 1l3 3-3 3M5 1l3 3-3 3" fill="none" stroke="#fff" stroke-width="1.4"/></svg></small></div>
  </article>
  <article class="abs card" style="left:870px">
    <div class="photo" role="img" aria-label="Bedroom with pillows and a bedside lamp with white shade" style="background:linear-gradient(90deg,#b9b2aa 0%,#6d5444 40%,#3b2418 70%,#5a3a28 100%)"></div>
    <div class="caption"><b>$10% OFF</b><small>SIGNUP <svg width="9" height="8" viewBox="0 0 9 8"><path d="M1 1l3 3-3 3M5 1l3 3-3 3" fill="none" stroke="#fff" stroke-width="1.4"/></svg></small></div>
  </article>

  <p class="abs card-text" style="left:211px">Bright Nook Wares provides beautiful and artistic home and hospitality lighting.</p>
  <p class="abs card-text" style="left:541px">Shopping at Bright Nook Wares is secured and protected by industry standard best practices.</p>
  <p class="abs card-text" style="left:871px">$10 off any purchase when you sign up for our newsletter.</p>

  <div class="abs footer-rule"></div>
  <div class="abs fcol" style="left:221px"><h3>HELP + INFO</h3><ul>
    <li>Contact us</li><li>Shipping info</li><li>Returns</li><li>To the trade</li><li>Privacy policy</li><li>Terms of use</li></ul></div>
  <div class="abs fdiv" style="left:364px"></div>
  <div class="abs fcol" style="left:408px"><h3>MY ACCOUNT</h3><ul>
    <li>Sign in</li><li>Order status</li><li>Order history</li><li>View cart</li><li>Checkout</li></ul></div>
  <div class="abs fdiv" style="left:541px"></div>
  <div class="abs fcol" style="left:586px"><h3>ABOUT</h3><ul>
    <li>Who we are</li><li>Testimonials</li></ul></div>
  <div class="abs fdiv" style="left:705px"></div>
  <div class="abs fcol" style="left:745px"><h3>CONTACT</h3>
    <p style="font-size:9.5px;color:#555">INFO@BRIGHTNOOKWARES.EXAMPLE</p></div>
  <div class="abs fdiv" style="left:904px"></div>
  <div class="abs fcol newsletter" style="left:941px;width:248px;height:120px"><h3>NEWSLETTER SIGNUP</h3>
    <p>Get the Monthly update from newsletter</p>
    <div class="email">ENTER YOUR EMAIL ID :</div>
    <div class="submit">SUBMIT</div></div>

  <div class="abs bottombar">
    <span class="copy">Copyrights © Bright Nook Wares 2013 | All Rights Reserved</span>
    <span class="follow">Follow Us :</span>
    <span class="social" style="left:865px;background:#2f66b3"></span>
    <span class="social" style="left:900px;background:#4fb0e0"></span>
    <span class="social" style="left:936px;background:#d7252c"></span>
  </div>

</div>
</body>
</html>
```